BrimFalcon Business Cards

We have a defined brand. Please visit our website to get a feel for the product and the color pallets. www.brimfalcon-demo.com

We need an updated, world class business card design. (See the attached existing card design). Please utilize BOTH sides of the card as shown and be creative with the layout. I do want the horse head icon to be positioned as it is with the existing card.

The remainder of the layout can be customized and I also want it vertically oriented.

Attached are the logo files and please use the colors as follows:
Green - #A5CE39
Tan - #CDBD99
Black

Feel free to play with the colors.

```html
<!DOCTYPE html>
<html lang="en">
<head>
<meta charset="UTF-8">
<title>BrimFalcon Business Cards</title>
<link href="https://fonts.googleapis.com/css2?family=Lato:wght@400;700&family=Open+Sans:wght@400;600&display=swap" rel="stylesheet">
<style>
  :root {
    --bg: #2a2a2a;
    --green-light: #b3d149;
    --green-mid: #7cb342;
    --green-dark: #3a8b3f;
    --band-green: #3d8d42;
    --icon-green: #3d8d42;
    --black: #111111;
    --ink: #222222;
    --white: #ffffff;
  }
  * { margin: 0; padding: 0; box-sizing: border-box; }
  html, body { width: 1200px; height: 960px; overflow: hidden; }
  body {
    background: var(--bg);
    display: flex;
    align-items: center;
    justify-content: center;
    gap: 80px;
    font-family: "Open Sans", sans-serif;
  }
  .card {
    width: 400px;
    height: 640px;
    border-radius: 28px;
    position: relative;
    overflow: hidden;
  }
  .card-front {
    background: linear-gradient(180deg, var(--green-light) 0%, var(--green-mid) 50%, var(--green-dark) 100%);
    display: flex;
    align-items: center;
    justify-content: center;
  }
  .front-brand {
    display: flex;
    align-items: center;
    gap: 12px;
  }
  .front-brand .brand-dot {
    width: 56px; height: 56px;
    border-radius: 50%;
    background: var(--black);
  }
  .front-brand .brand-name {
    font-weight: 600;
    font-size: 40px;
    color: var(--black);
    letter-spacing: 0.5px;
  }
  .card-back { background: var(--white); }
  .back-brand {
    position: absolute;
    top: 92px;
    right: 34px;
    text-align: right;
  }
  .back-brand .brand-line {
    display: flex;
    align-items: center;
    justify-content: flex-end;
    gap: 10px;
  }
  .back-brand .brand-dot {
    width: 34px; height: 34px;
    border-radius: 50%;
    background: var(--black);
  }
  .back-brand .brand-name {
    font-weight: 600;
    font-size: 34px;
    color: var(--black);
    line-height: 1;
  }
  .back-brand .brand-labs {
    font-weight: 600;
    font-size: 11px;
    color: var(--black);
    letter-spacing: 1px;
    margin-top: 4px;
  }
  .back-brand .tagline {
    font-size: 13px;
    letter-spacing: 3px;
    color: var(--ink);
    margin-top: 2px;
  }
  .name-band {
    position: absolute;
    top: 300px;
    left: 0;
    width: 290px;
    background: var(--band-green);
    color: var(--white);
    padding: 12px 20px 12px 52px;
    font-family: "Lato", sans-serif;
  }
  .name-band .person {
    font-weight: 700;
    font-size: 34px;
    line-height: 1.05;
  }
  .name-band .role {
    font-size: 21px;
    line-height: 1.1;
  }
  .contact-list {
    position: absolute;
    top: 470px;
    left: 36px;
    list-style: none;
  }
  .contact-list li {
    display: flex;
    align-items: center;
    gap: 12px;
    font-size: 19px;
    color: var(--ink);
    line-height: 1.55;
  }
  .contact-list svg { width: 14px; height: 14px; flex: none; fill: var(--icon-green); }
</style>
</head>
<body>
  <div class="card card-front">
    <div class="front-brand">
      <span class="brand-dot"></span>
      <span class="brand-name">BrimFalcon</span>
    </div>
  </div>

  <div class="card card-back">
    <div class="back-brand">
      <div class="brand-line">
        <span class="brand-dot"></span>
        <span class="brand-name">BrimFalcon</span>
      </div>
      <div class="brand-labs">LABS</div>
      <div class="tagline">Precision Built Motors</div>
    </div>

    <div class="name-band">
      <div class="person">Daniel Marsh</div>
      <div class="role">President &amp; CEO</div>
    </div>

    <ul class="contact-list">
      <li>
        <svg viewBox="0 0 16 16"><path d="M3.5 1 6 1.5 7 5 5.3 6.3c.8 1.8 2.4 3.4 4.4 4.4L11 9l3.5 1 .5 2.5-2 2C7 14 2 9 1.5 3z"/></svg>
        555.014.7391
      </li>
      <li>
        <svg viewBox="0 0 16 16"><path d="M1 3h14v1.5L8 9 1 4.5z M1 6l7 4.5L15 6v7H1z"/></svg>
        brimfalcon-demo.com
      </li>
      <li>
        <svg viewBox="0 0 16 16"><circle cx="8" cy="8" r="6.5" fill="none" stroke="#3d8d42" stroke-width="1.5"/><path d="M1.5 8h13M8 1.5c-3 3.5-3 9.5 0 13M8 1.5c3 3.5 3 9.5 0 13" fill="none" stroke="#3d8d42" stroke-width="1.2"/></svg>
        daniel@brimfalcon-demo.com
      </li>
      <li>
        <svg viewBox="0 0 16 16"><path d="M8 0C4.7 0 2.5 2.4 2.5 5.3 2.5 9 8 16 8 16s5.5-7 5.5-10.7C13.5 2.4 11.3 0 8 0zm0 7.5a2.2 2.2 0 1 1 0-4.4 2.2 2.2 0 0 1 0 4.4z"/></svg>
        Lakeview, Prairie Region
      </li>
    </ul>
  </div>
</body>
</html>
```